New Chartered Accounting Practice Needs Stationery Design

I need a new set of stationery including letterhead, business cards, envelopes and with compliments slips for a new Chartered Accounting Practice based in Melbourne, Victoria, Australia called "Marcus T. Brenholt, Chartered Accountant".
I will be providing Taxation Services, Accounting Services, Self-Managed Superannuation Fund Consulting and general consulting advice to small and medium business enterprises. I would like to see designs that use the colour blue. The final design should communicate trust, technical expertise and security.
Target Market(s)
English speaking, Australians. Proprietors of small and medium businesses - aged 30-65. Fellow professionals - lawyers, investment consultants, other accountants. Retirees - aged 60 and over
Industry/Entity Type
Business
Look and feel

```html
<!DOCTYPE html>
<html lang="en">
<head>
<meta charset="utf-8">
<title>Marcus T. Brenholt — Stationery Set</title>
<link href="https://fonts.googleapis.com/css2?family=Cinzel:wght@400;600&family=Open+Sans:wght@400&display=swap" rel="stylesheet">
<style>
  :root {
    --backdrop: #dcdcdc;
    --navy: #3b4455;
    --ink: #2b3446;
    --muted: #8a8f98;
    --paper: #ffffff;
    --faint: #d3d3d3;
    --serif: "Cinzel", "Times New Roman", serif;
    --sans: "Open Sans", Arial, sans-serif;
  }
  * { box-sizing: border-box; margin: 0; padding: 0; }
  html, body { width: 1200px; height: 900px; overflow: hidden; }
  body { background: var(--backdrop); position: relative; font-family: var(--sans); color: var(--ink); }

  .piece { position: absolute; }
  .paper { background: var(--paper); }
  .pattern { background: var(--navy); }

  /* wordmark: the practice name inside one plain square */
  .wordmark {
    position: absolute; display: flex; align-items: center; justify-content: center;
    background: var(--paper); font-family: var(--serif); font-weight: 600;
    color: var(--navy); letter-spacing: 0.02em;
  }
  .wordmark--faint { background: none; border: 2px solid var(--faint); color: var(--faint); }

  .masthead { position: absolute; text-align: right; }
  .masthead__name {
    font-family: var(--serif); font-weight: 600; color: var(--ink);
    letter-spacing: 0.03em; padding-bottom: 2px; border-bottom: 1px solid #b9bdc4;
    white-space: nowrap;
  }
  .masthead__title {
    font-size: 6.5px; color: var(--muted); letter-spacing: 0.12em; margin-top: 2px;
  }

  .contact { position: absolute; font-size: 5px; line-height: 1.45; color: var(--ink); white-space: nowrap; }

  /* business card back */
  .card-back { left: 40px; top: 40px; width: 207px; height: 118px; }
  .card-back .wordmark { left: 81px; top: 34px; width: 44px; height: 46px; font-size: 8px; }

  /* business card front */
  .card-front { left: 40px; top: 172px; width: 208px; height: 122px; }
  .card-front .masthead { right: 10px; top: 12px; }
  .card-front .masthead__name { font-size: 11px; }
  .card-front .masthead__title { font-size: 5.5px; }
  .card-front .contact { left: 11px; top: 84px; font-size: 4.2px; }
  .card-front .wordmark { left: 157px; top: 68px; width: 38px; height: 40px; font-size: 7px; }

  /* phone screen */
  .screen { left: 121px; top: 377px; width: 118px; height: 207px; }
  .screen .wordmark { left: 36px; top: 80px; width: 46px; height: 46px; font-size: 8px; }

  /* letterhead */
  .letter-back { left: 361px; top: 38px; width: 394px; height: 560px; }
  .letterhead { left: 278px; top: 97px; width: 377px; height: 560px; }
  .letterhead .masthead { right: 0; top: 20px; width: 377px; padding-right: 0; }
  .letterhead .masthead { right: 0; left: auto; }
  .letterhead .masthead__name { font-size: 14px; display: inline-block; }
  .letterhead .masthead { right: 0; }
  .letterhead .masthead__wrap { position: absolute; right: 0; top: 20px; }
  .letterhead .contact { left: 14px; top: 22px; }
  .letterhead .wordmark { left: 154px; top: 463px; width: 84px; height: 80px; font-size: 13px; }

  /* large mark */
  .mark-sheet { left: 877px; top: 103px; width: 160px; height: 160px; }
  .mark-sheet .wordmark { left: 10px; top: 10px; width: 140px; height: 140px; font-size: 24px; }

  /* presentation folder */
  .folder { left: 719px; top: 335px; width: 442px; height: 300px; }
  .folder .wordmark { left: 359px; top: 20px; width: 50px; height: 47px; font-size: 8px; }
  .folder__title {
    position: absolute; right: 20px; top: 258px; font-family: var(--serif);
    font-size: 21px; color: var(--paper); letter-spacing: 0.04em;
  }
  .folder__year { position: absolute; right: 22px; top: 284px; font-size: 6px; color: #aeb4bf; letter-spacing: 0.1em; }

  /* envelope */
  .envelope { left: 219px; top: 685px; width: 410px; height: 212px; overflow: hidden; }
  .envelope__flap { position: absolute; left: 0; top: 0; width: 410px; height: 48px; }
  .envelope .wordmark { left: 182px; top: 108px; width: 49px; height: 50px; font-size: 8px; }

  /* compliments slip */
  .slip { left: 663px; top: 685px; width: 418px; height: 212px; }
  .slip .masthead__wrap { position: absolute; right: 16px; top: 16px; }
  .slip .masthead__name { font-size: 13px; }
  .slip .contact { left: 14px; top: 186px; }
</style>
</head>
<body>

  <section class="piece card-back pattern" role="img" aria-label="Navy business card back with a fine scalloped pattern">
    <div class="wordmark">Brenholt</div>
  </section>

  <section class="piece card-front paper">
    <div class="masthead">
      <div class="masthead__name">Marcus T. Brenholt</div>
      <div class="masthead__title">CHARTERED ACCOUNTANT</div>
    </div>
    <div class="contact">
      Office: 14 Larch Street, Kew VIC 3101<br>
      Postal: PO Box 4410, Kew VIC 3101<br>
      Phone: 0412 308 716<br>
      Fax: (03) 9811 2047<br>
      Email: marcus@brenholtca.com.au
    </div>
    <div class="wordmark wordmark--faint">Brenholt</div>
  </section>

  <section class="piece screen pattern" role="img" aria-label="Navy phone wallpaper with a fine scalloped pattern">
    <div class="wordmark">Brenholt</div>
  </section>

  <div class="piece letter-back pattern" role="img" aria-label="Navy letterhead reverse with a fine scalloped pattern"></div>

  <section class="piece letterhead paper">
    <div class="contact">
      Office: 14 Larch Street, Kew VIC 3101<br>
      Postal: PO Box 4410, Kew VIC 3101<br>
      Phone: 0412 308 716<br>
      Fax: (03) 9811 2047<br>
      Email: marcus@brenholtca.com.au
    </div>
    <div class="masthead__wrap masthead" style="right:0;">
      <div class="masthead__name">Marcus T. Brenholt</div>
      <div class="masthead__title">CHARTERED ACCOUNTANT</div>
    </div>
    <div class="wordmark wordmark--faint">Brenholt</div>
  </section>

  <section class="piece mark-sheet paper">
    <div class="wordmark wordmark--faint">Brenholt</div>
  </section>

  <section class="piece folder pattern" role="img" aria-label="Navy presentation folder with a fine scalloped pattern">
    <div class="wordmark">Brenholt</div>
    <div class="folder__title">PRESENTATION</div>
    <div class="folder__year">2014</div>
  </section>

  <section class="piece envelope paper">
    <svg class="envelope__flap" viewBox="0 0 410 48" aria-hidden="true">
      <path d="M0 0 H410 V30 Q410 46 394 46 H16 Q0 46 0 30 Z" fill="#3b4455"/>
    </svg>
    <div class="wordmark wordmark--faint">Brenholt</div>
  </section>

  <section class="piece slip paper">
    <div class="masthead__wrap masthead">
      <div class="masthead__name">Marcus T. Brenholt</div>
      <div class="masthead__title">CHARTERED ACCOUNTANT</div>
    </div>
    <div class="contact">
      Office: 14 Larch Street, Kew VIC 3101<br>
      Postal: PO Box 4410, Kew VIC 3101
    </div>
  </section>

</body>
</html>
```